GivingGavelHub Website Redesign

I'm looking to give our website a new look and feel with better graphics/images and that is focused on conversions.
www.givinggavelhub.example. The content can stay the same. Im looking for a new hero section with maybe a call to auction form to create an auction by asking for the following information: Event Name, Event Benefits, Country, Time zone and currency.
Our goal is to show that we can host online auctions, mobile auctions and live in-person auction. The content does not need to change on the site. We just need sections or illustrations that represent those features. It would also be good to have a sections that will segment our users into the following categories: Nonprofits/Charities, Schools/Education, Businesses, Government Agency, Individual.
The following pages need to be updated:
https://www.givinggavelhub.example/
https://www.givinggavelhub.example/online-bidding-features
https://www.givinggavelhub.example/online-bidding-experience
https://www.givinggavelhub.example/about
https://www.givinggavelhub.example/pricing
Updates
This project would cover the following 4 pages:
https://www.givinggavelhub.example

```html
<!DOCTYPE html>
<html lang="en">
<head>
<meta charset="utf-8">
<title>GivingGavelHub – Online Charity Auctions</title>
<link href="https://fonts.googleapis.com/css2?family=Fredoka:wght@500;600&family=Poppins:wght@400;500;600&display=swap" rel="stylesheet">
<style>
:root{
  --blue:#1f5fc9;
  --blue-bright:#3b86ee;
  --navy:#0d3b8c;
  --ink:#1c1c2b;
  --text:#444a5a;
  --muted:#8a90a0;
  --light-bg:#eaf3fd;
  --faq-bg:#ececef;
  --footer:#141416;
  --white:#ffffff;
  --star:#f5a623;
}
*{box-sizing:border-box;margin:0;padding:0}
html,body{width:1200px;height:5042px;overflow:hidden}
body{font-family:'Poppins',sans-serif;color:var(--text);background:var(--white);position:relative}
.section{position:absolute;left:0;width:1200px}
.abs{position:absolute}
.heading{font-family:'Fredoka',sans-serif;font-weight:600;color:var(--navy);font-size:32px;text-align:center;line-height:40px}
.heading .accent{color:var(--blue-bright)}
.underline{position:absolute;left:50%;transform:translateX(-50%);width:70px;height:4px}
.underline::before,.underline::after{content:"";position:absolute;top:0;height:4px;border-radius:2px;background:var(--blue)}
.underline::before{left:0;width:42px}
.underline::after{right:0;width:20px}
.underline.white::before,.underline.white::after{background:var(--white)}
.pill{display:flex;align-items:center;justify-content:center;border-radius:20px;font-weight:600;font-size:12px;color:var(--white);background:var(--blue)}

/* header */
.header{top:0;height:130px;background:var(--white)}
.brand{display:flex;align-items:center;gap:10px;font-family:'Poppins',sans-serif;font-weight:600;color:var(--blue);font-size:24px}
.brand-mark{width:34px;height:34px;border-radius:50%;background:var(--blue)}
.toplinks{top:30px;left:623px;font-size:11px;color:var(--ink)}
.search{top:24px;left:848px;width:240px;height:32px;border:1.5px solid #1c1c2b;border-radius:16px;font-size:10px;color:var(--ink);padding:8px 14px}
.search-btn{position:absolute;right:3px;top:3px;width:24px;height:24px;border-radius:50%;background:var(--blue)}
.nav{top:92px;font-size:12px;color:var(--ink)}
.nav-active{font-weight:600}
.nav-line{top:68px;left:484px;width:36px;height:2px;background:var(--blue)}
.signin{top:84px;left:1000px;width:94px;height:32px}

/* hero */
.hero{top:130px;height:547px;background:linear-gradient(100deg,#dfe9fb 0%,#7fa8f2 45%,#2d6ae6 100%)}
.hero-art{left:30px;top:20px;width:640px;height:510px;border-radius:20px;background:radial-gradient(circle at 50% 45%,#c8b8f2 0%,#6c93ee 45%,rgba(40,100,230,0) 75%)}
.auction-card{left:706px;top:140px;width:426px;height:342px;background:var(--white);border-radius:14px}
.auction-card h2{position:absolute;top:34px;width:100%;text-align:center;font-family:'Fredoka',sans-serif;font-weight:600;font-size:38px;color:var(--navy)}
.auction-card h2 .accent{color:var(--blue-bright)}
.field{position:absolute;height:40px;border:1.5px solid #9aa0aa;font-size:11px;color:var(--ink);padding:11px 12px;display:flex;align-items:flex-start;gap:6px}
.field svg{flex:none;margin-top:2px}
.submit{position:absolute;left:166px;top:272px;width:94px;height:28px}

/* categories */
.categories{top:677px;height:420px}
.cat{position:absolute;top:169px;width:150px;text-align:center}
.cat-box{width:104px;height:104px;margin:0 auto;border-radius:12px;background:var(--white);box-shadow:0 4px 14px rgba(0,0,0,.12);display:flex;align-items:center;justify-content:center}
.cat-art{width:68px;height:60px;border-radius:8px}
.cat-label{margin-top:18px;font-size:15px;color:var(--ink);line-height:22px}

/* time band */
.timeband{top:1097px;height:678px;background:linear-gradient(90deg,#1c4d9a 0%,#1a55b0 50%,#1d4e9f 100%);color:var(--white);text-align:center}
.timeband .heading{color:var(--white)}
.timeband .sub{font-family:'Fredoka',sans-serif;font-weight:500;font-size:20px}
.timeband p{font-size:12px;line-height:22px}
.ghost-btn{border:1.5px solid var(--white);border-radius:16px;font-weight:600;font-size:12px;display:flex;align-items:center;justify-content:center}
.avatar{left:558px;top:379px;width:84px;height:84px;border-radius:50%;background:linear-gradient(#c79a86,#8c5f50);border:3px solid var(--white)}
.dots{display:flex;gap:10px;justify-content:center}
.dot{width:12px;height:12px;border-radius:50%;border:2px solid var(--white)}
.dot.on{background:var(--white)}

/* build */
.build{top:1775px;height:600px}
.build-card{top:201px;width:269px;height:319px;border-radius:4px;color:var(--white);font-family:'Fredoka',sans-serif;font-weight:600;font-size:20px}
.build-card .label{position:absolute;bottom:26px;width:100%;text-align:center}
.add-panel{position:absolute;left:16px;top:20px;right:16px;bottom:48px;background:rgba(24,74,160,.9);text-align:center;padding:30px 20px 0}
.add-panel h3{font-family:'Fredoka',sans-serif;font-weight:600;font-size:21px}
.add-panel p{font-family:'Poppins',sans-serif;font-weight:400;font-size:15px;line-height:27px;margin-top:14px}
.add-panel .more{display:inline-block;margin-top:8px;font-size:19px;border-bottom:3px solid var(--white);padding-bottom:2px}

/* support */
.support{top:2375px;height:498px;background:var(--light-bg)}
.support .heading{text-align:left}
.support-photo{left:686px;top:57px;width:370px;height:370px;border-radius:50%;background:radial-gradient(circle at 40% 35%,#d98b58 0%,#6b7280 45%,#2c3240 100%)}
.support-ring{left:676px;top:47px;width:390px;height:390px;border-radius:50%;border:2px solid var(--blue)}

/* company */
.company{top:2873px;height:347px}
.badge{position:absolute;top:3093px}

/* features */
.features{top:3220px;height:692px;background:linear-gradient(180deg,#1c58c4 0%,#2d73e4 100%)}
.features .heading{color:var(--white)}
.feature-card{top:257px;width:272px;height:299px;background:var(--white);border-radius:14px;text-align:center}
.feature-icon{width:76px;height:76px;border-radius:50%;background:var(--blue);margin:32px auto 0;display:flex;align-items:center;justify-content:center}
.feature-card h3{margin-top:24px;font-family:'Fredoka',sans-serif;font-weight:600;font-size:18px;color:var(--blue)}
.feature-card p{margin:10px auto 0;width:220px;font-size:11px;line-height:20px;color:var(--text)}
.feature-card .pill{width:96px;height:26px;margin:12px auto 0}

/* faq */
.faq{top:3912px;height:778px}
.faq-item{left:103px;width:991px;height:66px;background:var(--faq-bg);display:flex;align-items:center;padding:0 38px;justify-content:space-between;font-family:'Fredoka',sans-serif;font-weight:600;font-size:21px;color:var(--ink)}
.chev{width:28px;height:28px;border-radius:50%;background:var(--ink);display:flex;align-items:center;justify-content:center}
.faq-open{left:103px;width:991px;height:154px;background:var(--navy);color:var(--white);padding:20px 38px}
.faq-open .q{display:flex;justify-content:space-between;font-family:'Fredoka',sans-serif;font-weight:600;font-size:21px}
.faq-open p{margin-top:16px;font-size:12px;line-height:23px;width:830px}
.faq-open .chev{background:var(--white)}

/* footer */
.footer{top:4690px;height:352px;background:var(--footer);color:var(--white)}
.footer .brand{color:var(--white);font-size:30px;font-weight:500}
.footer .brand-mark{background:var(--white);width:40px;height:40px}
.social{width:36px;height:36px;border-radius:50%;background:var(--blue)}
.foot-col h4{font-family:'Fredoka',sans-serif;font-weight:600;font-size:21px}
.foot-col ul{list-style:none;margin-top:10px;font-size:13px;line-height:30px}
.contact-line{display:flex;gap:6px;align-items:flex-start;font-size:13px;line-height:22px}
.copyright{top:4990px;width:100%;text-align:center;font-size:9px;color:#cfcfcf}
</style>
</head>
<body>

<!-- Header -->
<header class="section header">
  <div class="abs brand" style="left:103px;top:48px"><span class="brand-mark"></span>GivingGavelHub</div>
  <div class="abs toplinks">For Bidders &nbsp;&nbsp;|&nbsp;&nbsp; For Fundraisers</div>
  <div class="abs search">Search auctions<span class="search-btn"><svg width="24" height="24" viewBox="0 0 24 24"><circle cx="11" cy="11" r="4" fill="none" stroke="#fff" stroke-width="1.6"/><line x1="14" y1="14" x2="17" y2="17" stroke="#fff" stroke-width="1.6"/></svg></span></div>
  <div class="abs nav-line"></div>
  <nav>
    <span class="abs nav nav-active" style="left:484px">Home</span>
    <span class="abs nav" style="left:560px">How It Works</span>
    <span class="abs nav" style="left:672px">Pricing</span>
    <span class="abs nav" style="left:752px">About</span>
    <span class="abs nav" style="left:826px">Blog</span>
    <span class="abs nav" style="left:890px">Contact Us</span>
  </nav>
  <div class="abs pill signin">Sign In ⌄</div>
</header>

<!-- Hero -->
<section class="section hero">
  <div class="abs hero-art" role="img" aria-label="Illustration of two phones with a hand passing a coin to another hand"></div>
  <form class="abs auction-card">
    <h2>Build An <span class="accent">Auction</span></h2>
    <div class="field" style="left:28px;top:92px;width:178px"><svg width="9" height="10" viewBox="0 0 9 10"><circle cx="4.5" cy="2.5" r="2.5" fill="#1c1c2b"/><path d="M0 10a4.5 4 0 0 1 9 0z" fill="#1c1c2b"/></svg>Event Name</div>
    <div class="field" style="left:220px;top:92px;width:178px"><svg width="10" height="10" viewBox="0 0 10 10"><rect x="1" y="4" width="8" height="6" fill="#1c1c2b"/><rect x="0" y="2" width="10" height="3" fill="#1c1c2b"/></svg>Event Benefits</div>
    <div class="field" style="left:28px;top:150px;width:178px"><svg width="10" height="10" viewBox="0 0 10 10"><circle cx="5" cy="5" r="5" fill="#1c1c2b"/></svg>Country</div>
    <div class="field" style="left:220px;top:150px;width:178px"><svg width="10" height="10" viewBox="0 0 10 10"><circle cx="5" cy="5" r="4" fill="none" stroke="#1c1c2b" stroke-width="1.4"/><path d="M5 2.5V5h2" stroke="#1c1c2b" fill="none"/></svg>Time Zone</div>
    <div class="field" style="left:28px;top:204px;width:370px;justify-content:space-between"><span>$ &nbsp;Currency</span><span>⌄</span></div>
    <div class="pill submit">Submit</div>
  </form>
</section>

<!-- Categories -->
<section class="section categories">
  <h2 class="heading abs" style="top:68px;width:100%">Charity <span class="accent">Categories</span></h2>
  <div class="underline" style="top:123px"></div>
  <div class="cat" style="left:127px"><div class="cat-box"><div class="cat-art" role="img" aria-label="Colourful people-circle icon" style="background:linear-gradient(135deg,#e8523f,#2f8fd8,#3bb36b)"></div></div><div class="cat-label">Nonprofits<br>Charities</div></div>
  <div class="cat" style="left:327px"><div class="cat-box"><div class="cat-art" role="img" aria-label="Hands with pencils icon" style="background:linear-gradient(135deg,#e06a4a,#4a7bd1)"></div></div><div class="cat-label">Schools<br>Education</div></div>
  <div class="cat" style="left:525px"><div class="cat-box"><div class="cat-art" role="img" aria-label="Business team with growth chart icon" style="background:linear-gradient(135deg,#8db3ef,#2a55b8)"></div></div><div class="cat-label" style="margin-top:28px">Businesses</div></div>
  <div class="cat" style="left:723px"><div class="cat-box"><div class="cat-art" role="img" aria-label="Government office workers icon" style="background:linear-gradient(135deg,#7a8597,#2d3340)"></div></div><div class="cat-label" style="margin-top:14px">Government<br>Agencies</div></div>
  <div class="cat" style="left:923px"><div class="cat-box"><div class="cat-art" role="img" aria-label="Individual person icon" style="background:linear-gradient(135deg,#cfd4dc,#7d8594);border-radius:50%;width:60px"></div></div><div class="cat-label" style="margin-top:28px">Individuals</div></div>
</section>

<!-- Spend less time band -->
<section class="section timeband" role="region">
  <div class="abs" role="img" aria-label="Faded photo of a person with a donate box and laptop" style="left:0;top:0;width:420px;height:678px;background:linear-gradient(90deg,rgba(255,255,255,.08),rgba(255,255,255,0))"></div>
  <h2 class="heading abs" style="top:105px;width:100%;line-height:40px">Spend less time.<br>Make more money.</h2>
  <div class="underline white" style="top:193px"></div>
  <div class="abs sub" style="top:216px;width:100%">Quickly Create, Design And Manage Auctions</div>
  <p class="abs" style="top:256px;left:190px;width:820px">You are only 5 minutes away from having your auction built and ready for items. We took the pain and confusion out of getting started.</p>
  <div class="abs ghost-btn" style="left:541px;top:322px;width:118px;height:30px">How It Works</div>
  <div class="abs avatar" role="img" aria-label="Portrait of a smiling customer"></div>
  <p class="abs" style="top:476px;left:240px;width:720px">"I'm 74 years old and I didn't need to call my Grandkids to set up this auction for me! The software was easy to use and the end of auction experience was a breeze!"</p>
  <div class="abs" style="top:526px;width:100%;font-size:10px;font-weight:600">Marion L. - Lakeside Civic Club</div>
  <div class="abs" style="top:548px;width:100%;font-size:13px;color:var(--star);letter-spacing:1px">★★★★☆</div>
  <div class="abs dots" style="top:600px;width:100%"><span class="dot"></span><span class="dot on"></span><span class="dot on"></span></div>
</section>

<!-- Build in minutes -->
<section class="section build">
  <h2 class="heading abs" style="top:67px;width:100%">Build Your Auction In Minutes,<br><span class="accent">Not Days.</span></h2>
  <div class="underline" style="top:158px"></div>
  <div class="abs build-card" style="left:151px" role="img" aria-label="Photo of a team meeting around a table"><div style="position:absolute;inset:0;border-radius:4px;background:linear-gradient(180deg,#9fb6d2 0%,#3c6bb5 70%,#1e4f9e 100%)"></div><div class="label">Build</div></div>
  <div class="abs build-card" style="left:466px;background:linear-gradient(135deg,#c9ced6,#5d6a80)" role="img" aria-label="Photo of a person typing on a laptop"><div class="add-panel"><h3>Add</h3><p>Upload items in bulk or add them one at a time. Our item wizard will walk you through the process.</p><span class="more">Learn More</span></div></div>
  <div class="abs build-card" style="left:780px" role="img" aria-label="Illustration of a hand holding a glowing growth chart"><div style="position:absolute;inset:0;border-radius:4px;background:linear-gradient(160deg,#3b4f7a 0%,#1a2b52 60%,#0e1a35 100%)"></div><div class="label">Share</div></div>
</section>

<!-- Support -->
<section class="section support">
  <h2 class="heading abs" style="left:103px;top:125px">Friendly Technical Support<br><span class="accent">And Training When You Need It.</span></h2>
  <div class="underline" style="top:222px;left:103px;transform:none"></div>
  <p class="abs" style="left:103px;top:249px;width:480px;font-size:15px;line-height:24px;color:var(--ink)">Other companies charge hundreds of dollars for your auction support and training. We offer it for free.</p>
  <div class="abs pill" style="left:103px;top:327px;width:132px;height:28px">Schedule a Call</div>
  <div class="abs support-ring"></div>
  <div class="abs support-photo" role="img" aria-label="Photo of a support agent wearing a headset at a computer"></div>
</section>

<!-- Good company -->
<section class="section company">
  <h2 class="heading abs" style="top:70px;width:100%">You're In Good Company</h2>
  <div class="underline" style="top:118px"></div>
  <div class="abs" style="left:233px;top:198px;width:44px;height:44px;background:#3f8fd9;border-radius:4px" role="img" aria-label="Partner badge"></div>
  <div class="abs" style="left:451px;top:186px;width:68px;height:68px;border-radius:50%;border:3px solid #8a6fa8" role="img" aria-label="Partner badge"></div>
  <div class="abs" style="left:665px;top:170px;width:100px;height:100px;border-radius:50%;background:#fff;box-shadow:0 4px 16px rgba(0,0,0,.15)"><div style="margin:26px auto;width:48px;height:48px;border-radius:50%;background:#e45a1f" role="img" aria-label="Partner badge"></div></div>
  <div class="abs" style="left:917px;top:190px;width:58px;height:58px;background:#c9a23a;border-radius:4px" role="img" aria-label="Partner badge"></div>
</section>

<!-- Features -->
<section class="section features">
  <h2 class="heading abs" style="top:108px;left:100px;width:1000px">Every Charity Auction Comes Packed With All The Features You Need To Run A Live Event Too.</h2>
  <div class="underline white" style="top:203px"></div>
  <div class="abs feature-card" style="left:132px"><div class="feature-icon"><svg width="36" height="36" viewBox="0 0 36 36"><rect x="8" y="6" width="18" height="24" rx="2" fill="none" stroke="#fff" stroke-width="2.5"/><line x1="12" y1="13" x2="22" y2="13" stroke="#fff" stroke-width="2.5"/><line x1="12" y1="19" x2="22" y2="19" stroke="#fff" stroke-width="2.5"/><path d="M24 22l6-6 3 3-6 6h-3z" fill="#fff"/></svg></div><h3>Pre-Register Guests</h3><p>When you pre-register your guests, this gets everyone set up for the auction before it begins.</p><div class="pill">Read More</div></div>
  <div class="abs feature-card" style="left:478px"><div class="feature-icon"><svg width="40" height="36" viewBox="0 0 40 36"><circle cx="20" cy="14" r="6" fill="none" stroke="#fff" stroke-width="2.5"/><circle cx="20" cy="14" r="2" fill="#fff"/><rect x="6" y="24" width="6" height="8" fill="#fff"/><rect x="17" y="24" width="6" height="8" fill="#fff"/><rect x="28" y="24" width="6" height="8" fill="#fff"/></svg></div><h3>Attendee Management</h3><p>Manage your attendee communications via your GivingGavelHub dashboard.</p><div class="pill">Read More</div></div>
  <div class="abs feature-card" style="left:824px"><div class="feature-icon"><svg width="36" height="36" viewBox="0 0 36 36"><circle cx="20" cy="12" r="7" fill="#fff"/><text x="20" y="16" text-anchor="middle" font-size="10" font-weight="700" fill="#1f5fc9" font-family="Poppins,sans-serif">$</text><path d="M4 26h8l6 3h10l4-4v-1H22l-2 2h-6" fill="none" stroke="#fff" stroke-width="2.5"/></svg></div><h3>Accept Donations</h3><p>We have integrated payment systems so you can accept donations via credit card, check, QuickPayz, and more.</p><div class="pill">Read More</div></div>
  <div class="abs dots" style="top:612px;width:100%"><span class="dot"></span><span class="dot on"></span><span class="dot on"></span></div>
</section>

<!-- FAQ -->
<section class="section faq">
  <h2 class="heading abs" style="top:78px;width:100%">Frequently Asked <span class="accent">Questions</span></h2>
  <div class="underline" style="top:126px"></div>
  <div class="abs faq-item" style="top:174px">Can I Pass Fees Onto Bidders?<span class="chev"><svg width="12" height="8" viewBox="0 0 12 8"><path d="M1 1l5 5 5-5" fill="none" stroke="#fff" stroke-width="2"/></svg></span></div>
  <div class="abs faq-item" style="top:254px">What Happens If Items Don't Sell?<span class="chev"><svg width="12" height="8" viewBox="0 0 12 8"><path d="M1 1l5 5 5-5" fill="none" stroke="#fff" stroke-width="2"/></svg></span></div>
  <div class="abs faq-item" style="top:334px">Can I Download All My Bidder Data?<span class="chev"><svg width="12" height="8" viewBox="0 0 12 8"><path d="M1 1l5 5 5-5" fill="none" stroke="#fff" stroke-width="2"/></svg></span></div>
  <div class="abs faq-open" style="top:414px"><div class="q">What Is The Management Fee?<span class="chev"><svg width="12" height="8" viewBox="0 0 12 8"><path d="M1 1l5 5 5-5" fill="none" stroke="#0d3b8c" stroke-width="2"/></svg></span></div><p>The management fee is a fee we charge to use our platform. If you select our free plan, we will charge a 5% management fee of the total amount raised. For example, if your auction raises $1000, we will collect a $50 management fee. Depending on your auction goals and size, you could limit management fees by choosing a prepaid plan.</p></div>
  <div class="abs faq-item" style="top:582px">Can You Mail Me A Check?<span class="chev"><svg width="12" height="8" viewBox="0 0 12 8"><path d="M1 1l5 5 5-5" fill="none" stroke="#fff" stroke-width="2"/></svg></span></div>
  <div class="abs pill" style="left:550px;top:676px;width:100px;height:30px">View More</div>
</section>

<!-- Footer -->
<footer class="section footer">
  <div class="abs brand" style="left:103px;top:78px"><span class="brand-mark"></span>GivingGavelHub</div>
  <div class="abs social" style="left:106px;top:144px"></div>
  <div class="abs social" style="left:156px;top:144px"></div>
  <div class="abs social" style="left:206px;top:144px"></div>
  <div class="abs social" style="left:256px;top:144px"></div>
  <div class="abs foot-col" style="left:567px;top:52px"><h4>Quick Link</h4><ul><li>Home</li><li>How It Works</li><li>Pricing</li><li>About</li><li>Blog</li><li>Contact Us</li></ul></div>
  <div class="abs foot-col" style="left:725px;top:52px"><h4>Auctions</h4><ul><li>Silent Auctions</li><li>Browse Auctions</li></ul></div>
  <div class="abs foot-col" style="left:890px;top:52px;width:240px"><h4>Contact Us</h4>
    <div class="contact-line" style="margin-top:14px"><svg width="10" height="14" viewBox="0 0 10 14" style="margin-top:4px"><path d="M5 0a5 5 0 0 1 5 5c0 4-5 9-5 9S0 9 0 5a5 5 0 0 1 5-5z" fill="#fff"/><circle cx="5" cy="5" r="2" fill="#141416"/></svg><span>Lorem ipsum dolor sit amet, sed do eiusmod</span></div>
    <div class="contact-line" style="margin-top:14px"><svg width="12" height="12" viewBox="0 0 12 12" style="margin-top:5px"><path d="M2 0l3 3-1.5 2a7 7 0 0 0 3.5 3.5L9 7l3 3-2 2C5 12 0 7 0 2z" fill="#fff"/></svg><span>+1 555 010 2040</span></div>
    <div class="contact-line" style="margin-top:14px"><svg width="14" height="10" viewBox="0 0 14 10" style="margin-top:6px"><rect width="14" height="10" fill="#fff"/><path d="M0 0l7 6 7-6" fill="none" stroke="#141416" stroke-width="1.2"/></svg><span>info@givinggavelhub.example</span></div>
  </div>
  <div class="abs copyright" style="top:300px">© ALL RIGHTS RESERVED, 2023, GIVINGGAVELHUB &nbsp;|&nbsp; ALL RIGHTS RESERVED</div>
</footer>

</body>
</html>
```